Brighten up our Patty Hut Retail Menus

We are a large family-run, food company located in Papua New Guinea and sell a wide range of products. We have 3x Comet Patty Huts and all items are in-house manufactured by our Butchery and Bakery. We are fun, bold and colourful! The Comet Patty colours are Blue and Yellow and our overarching company colours are Red and Black.

Our current menu board is attached in size 120cm (h) x 200cm(w).
Our menu is for display in our retail in 2 sizes (portrait and landscape) and online. We currently feel this is too dark, messy and difficult to read. We want to target our customer base - where photos are a key point for sales! Font and size need to be readable from afar. Text content/grouping should be the same as our previous one. We also want to keep it modern. We are open to a variety of original designs/layouts.

Logos, photos and menu items are attached.
Follow our website - www.klq.com.pg for more information.

Please don't hesitate to ask any questions! Thank you and we can't wait for you to join our project.

Target Market(s)

Economical

Industry/Entity Type

Fast Food

Colors
0054AA
0677BA
7BADD7
CADEEF
E8F1F8
FFF300
FFF600
FEFA6F
FFFEC7
FFFEE8

Requirements
Must have
• Images as the key point of sale, clear to read.
Nice to have
• Inviting, bright, bold, playful
Should not have
• Dark, difficult to read

```html
<!DOCTYPE html>
<html lang="en">
<head>
<meta charset="utf-8">
<title>Comet Patty Huts – Menu Board</title>
<link rel="stylesheet" href="https://fonts.googleapis.com/css2?family=Bebas+Neue&family=Oswald:wght@400;500;600;700&family=Roboto+Condensed:wght@400;700&display=swap">
<style>
  :root{
    --blue:#0054aa;
    --blue-mid:#0677ba;
    --sky:#7badd7;
    --yellow:#fff300;
    --orange:#f5a31a;
    --green:#1b9a48;
    --maroon:#7a1d2c;
    --cyan:#1a9ad6;
    --red:#e6322a;
    --drinks:#1f8a3b;
    --ink:#1d2d50;
    --paper:#ffffff;
    --photo-warm:#d98b3a;
    --photo-bun:#e7a24c;
  }
  *{box-sizing:border-box;margin:0;padding:0}
  html,body{width:1200px;height:1014px;overflow:hidden;background:var(--paper)}
  body{font-family:"Roboto Condensed",Arial,sans-serif;color:var(--ink)}
  .menu-board{width:1200px;height:1014px;display:grid;grid-template-columns:340px 270px 275px 315px;background:var(--paper)}
  .column{position:relative;height:1014px;display:flex;flex-direction:column;overflow:hidden}
  .column + .column{border-left:3px dotted var(--sky)}
  .section-bar{font-family:"Bebas Neue",Impact,sans-serif;color:#fff;font-size:30px;letter-spacing:1px;text-align:center;height:46px;line-height:48px;flex:none;font-weight:400}
  .section-bar small{font-size:14px;margin-left:4px}
  .bar-blue{background:var(--blue)}
  .bar-orange{background:var(--orange)}
  .bar-maroon{background:var(--maroon);font-size:20px;height:30px;line-height:32px}
  .bar-cyan{background:var(--cyan);font-size:20px;height:30px;line-height:32px}
  .bar-red{background:var(--red);font-size:22px;height:32px;line-height:34px}
  .bar-green{background:var(--drinks);font-size:22px;height:32px;line-height:34px}
  .group-title{font-family:"Oswald",Arial,sans-serif;font-weight:700;color:var(--green);font-size:24px;text-align:center;line-height:1.1;text-transform:uppercase;margin:6px 10px 2px}
  .item-row{display:grid;grid-template-columns:88px 1fr;gap:10px;padding:4px 12px;align-items:start}
  .photo{border-radius:10px;background:radial-gradient(circle at 50% 45%,var(--photo-bun),var(--photo-warm) 70%,#b4652a)}
  .photo.sandwich{height:52px;margin-top:6px;border-radius:6px}
  .photo.muffin{height:56px;margin-top:4px;border-radius:40%}
  .photo.hash{height:50px;margin-top:4px;background:radial-gradient(circle,#f6cf55,#e1a32d)}
  .item-name{font-family:"Oswald",Arial,sans-serif;font-weight:600;color:var(--orange);font-size:20px;line-height:1.1}
  .item-desc{font-size:10px;font-weight:700;text-transform:uppercase;line-height:1.25;color:var(--blue);margin-top:2px;max-width:146px}
  .price{display:inline-block;background:var(--blue);color:#fff;font-family:"Oswald",Arial,sans-serif;font-weight:600;font-size:15px;padding:2px 7px;transform:rotate(-4deg);border-radius:2px;white-space:nowrap}
  .item-body{position:relative;min-height:60px}
  .item-body .price{position:absolute;right:0;bottom:2px}
  .dots{border-top:3px dotted var(--blue);margin:4px 14px}

  .meal-deal{display:flex;gap:8px;align-items:center;margin:8px 12px 8px}
  .meal-deal-badge{background:var(--blue);color:var(--yellow);font-family:"Bebas Neue",Impact,sans-serif;width:80px;height:80px;flex:none;display:flex;flex-direction:column;align-items:center;justify-content:center;font-size:26px;line-height:.9;text-align:center}
  .meal-deal-badge span{display:block;color:#fff;font-family:"Oswald",Arial,sans-serif;font-size:13px;line-height:1;margin-bottom:3px}
  .meal-deal-text{font-size:9px;font-weight:700;color:var(--blue);text-transform:uppercase;line-height:1.2;width:110px}
  .meal-deal-text .save{font-family:"Oswald",Arial,sans-serif;font-size:20px;color:var(--blue);display:block;margin-top:2px}
  .meal-deal-text .note{color:var(--orange)}
  .just-add{border:3px solid var(--blue);font-family:"Oswald",Arial,sans-serif;text-align:center;padding:4px 6px;color:var(--orange);font-size:20px;line-height:1}
  .just-add b{display:block;color:var(--blue);font-size:24px;font-weight:700}
  .just-add b small{font-size:12px}

  .extras{margin-top:auto;display:grid;grid-template-columns:110px 230px}
  .extras .section-bar{font-size:22px;height:32px;line-height:34px}
  .extras-list{padding:8px 8px 10px;font-family:"Oswald",Arial,sans-serif;font-size:11.5px;color:var(--orange);line-height:1.5}
  .extras-list .price{font-size:9.5px;padding:0 4px;transform:none}
  .sauce-list{display:flex;flex-direction:column;align-items:flex-start;gap:4px}
  .addon-grid{display:grid;grid-template-columns:94px 1fr;column-gap:12px}
  .addon-col{display:flex;flex-direction:column;gap:2px}
  .addon-col div{display:flex;justify-content:space-between;align-items:center;white-space:nowrap;gap:4px}

  .box-item{display:grid;grid-template-columns:74px 1fr;gap:8px;padding:8px 10px 6px}
  .box-item .photo{height:56px}
  .box-item .item-name{font-size:20px}
  .box-item .item-desc{font-size:9px;max-width:150px}
  .box-item .price{float:right;margin-top:-2px}
  .bucket{text-align:center;padding:6px 12px 8px;font-family:"Oswald",Arial,sans-serif}
  .bucket h3{color:var(--orange);font-size:30px;font-weight:600;margin-bottom:14px}
  .bucket p{color:var(--blue);font-size:15px;font-weight:500;line-height:1.3;text-transform:uppercase}
  .bucket .upgrade{color:var(--orange);font-size:10px;margin-top:2px}
  .bucket .big{font-size:22px;font-weight:600;line-height:1.15}
  .kids{display:grid;grid-template-columns:70px 1fr;gap:8px;padding:10px 12px;align-items:center}
  .kids .photo{height:76px;background:linear-gradient(160deg,var(--blue-mid),var(--blue));border-radius:6px}
  .kids-title{font-family:"Bebas Neue",Impact,sans-serif;font-size:44px;color:var(--red);letter-spacing:1px;line-height:1;font-weight:400}
  .kids-desc{font-size:11px;font-weight:700;color:var(--blue);text-transform:uppercase;line-height:1.3}
  .kids-burgers{padding:6px 12px 0;text-align:center}
  .kids-burgers .item-name{display:flex;justify-content:center;gap:10px;align-items:center;font-size:19px}
  .trio{display:flex;justify-content:space-between;margin-top:10px}
  .trio .photo{width:70px;height:58px;border-radius:50% 50% 40% 40%}

  .burger-grid{display:grid;grid-template-columns:1fr 1fr;gap:4px 6px;padding:8px 8px 4px}
  .burger{display:flex;flex-direction:column;align-items:flex-start}
  .burger .item-name{font-size:18px;white-space:nowrap}
  .burger-pic{display:flex;align-items:center;gap:6px;margin-top:4px}
  .burger-pic .photo{width:48px;height:46px;border-radius:50% 50% 40% 40%}
  .upgrade-box{display:grid;grid-template-columns:70px 1fr;gap:6px;padding:6px 10px;border-top:3px dotted var(--blue);margin:4px 8px 8px}
  .upgrade-box .photo{height:70px;background:radial-gradient(circle,#f7c64a,#e08a1e)}
  .upgrade-line{display:flex;justify-content:space-between;align-items:center;font-family:"Oswald",Arial,sans-serif;color:var(--orange);font-size:12px;line-height:1.1;margin-bottom:4px}
  .upgrade-line .price{font-size:11px;padding:1px 4px}
  .upgrade-note{font-size:8px;color:var(--blue);font-weight:700;text-transform:uppercase}
  .mini-row{display:grid;grid-template-columns:repeat(3,1fr);gap:4px;padding:8px 6px}
  .mini-row.two{grid-template-columns:1fr 1fr}
  .mini{text-align:center;font-family:"Oswald",Arial,sans-serif;color:var(--orange);font-size:12px}
  .mini-pic{display:flex;align-items:center;justify-content:center;gap:4px;margin-top:4px}
  .mini-pic .photo{width:40px;height:32px;border-radius:6px}
  .mini .price{font-size:11px;padding:1px 4px}

  .dessert{display:grid;grid-template-columns:1fr 1fr;padding:10px 10px 2px;gap:6px}
  .dessert-item{display:flex;gap:6px;align-items:center}
  .dessert-item .photo{width:34px;height:86px;border-radius:40% 40% 10% 10%;background:linear-gradient(#fbf4e6,#e9dcc2)}
  .dessert-item .photo.cone{background:linear-gradient(#fbf4e6 55%,#d99b4c 55%)}
  .dessert-item .item-name{font-size:18px}
  .dessert-item .price{font-size:12px;padding:1px 5px}
  .dessert-addons{display:grid;grid-template-columns:1fr 56px;gap:6px;padding:4px 12px 8px;align-items:center}
  .dessert-addons h4{font-family:"Oswald",Arial,sans-serif;color:var(--orange);font-size:15px;font-weight:600}
  .dessert-addons p{font-size:9px;color:var(--blue);font-weight:700;line-height:1.3}
  .badge{width:50px;height:50px;border-radius:50%;border:3px solid var(--blue-mid);background:var(--yellow)}
  .drink-list{list-style:none;padding:8px 18px 8px 26px}
  .drink-list li{display:flex;justify-content:space-between;align-items:center;font-family:"Oswald",Arial,sans-serif;color:var(--orange);font-size:15px;line-height:1.55}
  .drink-list .price{font-size:12px;padding:0 5px;transform:none}
  .drink-list.cold li{font-size:12.5px;line-height:1.45}
  .drink-list.cold .price{font-size:10px}
</style>
</head>
<body>
<main class="menu-board">

  <section class="column breakfast">
    <h2 class="section-bar bar-blue">Breakfast</h2>
    <h3 class="group-title">Brekkie Toastie</h3>

    <article class="item-row">
      <div class="photo sandwich" role="img" aria-label="Photo of a toasted chicken and cheese sandwich"></div>
      <div class="item-body">
        <h4 class="item-name">Chicken &amp; Cheese</h4>
        <p class="item-desc">Roast chicken with grilled cheese, toasted on our bakery bread</p>
        <span class="price">K13.00</span>
      </div>
    </article>
    <article class="item-row">
      <div class="photo sandwich" role="img" aria-label="Photo of a toasted ham and cheese sandwich"></div>
      <div class="item-body">
        <h4 class="item-name">Ham &amp; Cheese</h4>
        <p class="item-desc">Ham and melted cheese, toasted fresh on bakery bread</p>
        <span class="price">K13.00</span>
      </div>
    </article>
    <article class="item-row">
      <div class="photo sandwich" role="img" aria-label="Photo of a maple ham and cheese croissant"></div>
      <div class="item-body">
        <h4 class="item-name">Maple Ham &amp; Cheese Croissant</h4>
        <p class="item-desc">Maple ham with melted cheese in a fresh toasted croissant</p>
        <span class="price">K12.00</span>
      </div>
    </article>

    <div class="dots"></div>
    <h3 class="group-title">Cometty Breakfast<br>Muffin</h3>

    <article class="item-row">
      <div class="photo muffin" role="img" aria-label="Photo of a sausage and egg muffin"></div>
      <div class="item-body">
        <h4 class="item-name">Sausages &amp; Egg Muffin</h4>
        <p class="item-desc">Toasted English muffin with sausage patty, fried egg and cheese</p>
        <span class="price">K12.00</span>
      </div>
    </article>
    <article class="item-row">
      <div class="photo muffin" role="img" aria-label="Photo of a bacon and egg muffin"></div>
      <div class="item-body">
        <h4 class="item-name">Bacon &amp; Egg Muffin</h4>
        <p class="item-desc">Bacon, egg and cheese with BBQ sauce on a toasted muffin</p>
        <span class="price">K12.00</span>
      </div>
    </article>
    <article class="item-row">
      <div class="photo hash" role="img" aria-label="Photo of two golden hash browns"></div>
      <div class="item-body">
        <h4 class="item-name">Hash Browns</h4>
        <p class="item-desc">2 x crunchy potato deliciousness</p>
        <span class="price">K5.00</span>
      </div>
    </article>

    <div class="meal-deal">
      <div class="meal-deal-badge"><span>Brekky</span>Meal<br>Deal</div>
      <p class="meal-deal-text">Make your breakfast item a meal with coffee or hot chocolate<br><span class="note">(This means that's all)</span><span class="save">Save K2.50</span></p>
      <div class="just-add">Just Add<b>K8.00<small>Tasol</small></b></div>
    </div>

    <div class="extras">
      <div>
        <h3 class="section-bar bar-orange">Dipping Sauce</h3>
        <div class="extras-list sauce-list">
          <div>Tomato<br>BBQ<br>Comet Hot<br>Garlic Aioli<br>Sweet Chili</div>
          <span class="price">K3.00 each</span>
        </div>
      </div>
      <div>
        <h3 class="section-bar bar-blue">Add On's</h3>
        <div class="extras-list addon-grid">
          <div class="addon-col">
            <div>Cheese slice <span class="price">K2.00</span></div>
            <div>Onion rings <span class="price">K3.00</span></div>
            <div>Beetroot slice <span class="price">K2.00</span></div>
            <div>Bacon <span class="price">K3.00</span></div>
            <div>Egg <span class="price">K3.00</span></div>
          </div>
          <div class="addon-col">
            <div>Extra beef patty <span class="price">K8.00</span></div>
            <div>Extra lamb patty <span class="price">K10.00</span></div>
            <div>Extra sauce <span class="price">K2.00</span></div>
          </div>
        </div>
      </div>
    </div>
  </section>

  <section class="column boxes">
    <h2 class="section-bar bar-orange">Comet Boxes</h2>

    <article class="box-item">
      <div class="photo" role="img" aria-label="Photo of chicken nibbles and chips in a box"></div>
      <div>
        <h4 class="item-name">Comet Nibbles &amp; Chips</h4>
        <p class="item-desc">10 pieces of fried chicken nibbles with chips and dipping sauce</p>
        <span class="price">K40.00</span>
      </div>
    </article>
    <article class="box-item">
      <div class="photo" role="img" aria-label="Photo of three pieces of fried chicken"></div>
      <div>
        <h4 class="item-name">3 Pc Chicken</h4>
        <p class="item-desc">3 tender pieces of southern fried chicken served with chips, crispy and golden</p>
        <span class="price">K36.00</span>
      </div>
    </article>
    <article class="box-item">
      <div class="photo" role="img" aria-label="Photo of chicken nuggets"></div>
      <div>
        <h4 class="item-name">Chicken Nuggets</h4>
        <p class="item-desc">6 chicken nuggets with dipping sauce</p>
        <span class="price">K15.00</span>
      </div>
    </article>

    <div class="bucket">
      <h3>Chicken Bucket</h3>
      <p>18 pcs of southern fried chicken</p>
      <p>2 x large chips, 1 x 1 ltr soft drink, 1 x coleslaw</p>
      <p class="upgrade">Upgrade your chicken bucket to a family meal deal</p>
      <p class="big">K45.00 Tasol<br>K125.00 Tasol</p>
    </div>

    <div class="kids">
      <div class="photo" role="img" aria-label="Photo of a kids meal box with juice and toy"></div>
      <div>
        <h3 class="kids-title">Kids Meal</h3>
        <p class="kids-desc">Kids burger comes with juice box, small chips and a toy</p>
      </div>
    </div>
    <div class="kids-burgers">
      <h4 class="item-name">Chicken / Beef / Fish <span class="price">K22.00</span></h4>
      <div class="trio">
        <div class="photo" role="img" aria-label="Photo of a small chicken burger"></div>
        <div class="photo" role="img" aria-label="Photo of a small beef burger"></div>
        <div class="photo" role="img" aria-label="Photo of a small fish burger"></div>
      </div>
    </div>
  </section>

  <section class="column burgers">
    <h2 class="section-bar bar-blue">Burgers, Wraps <small>&amp; more</small></h2>
    <div class="burger-grid">
      <article class="burger"><h4 class="item-name">Cheese Burger</h4><div class="burger-pic"><div class="photo" role="img" aria-label="Photo of a cheese burger"></div><span class="price">K20.00</span></div></article>
      <article class="burger"><h4 class="item-name">Aussie Burger</h4><div class="burger-pic"><div class="photo" role="img" aria-label="Photo of an aussie burger"></div><span class="price">K25.00</span></div></article>
      <article class="burger"><h4 class="item-name">Kiwi Deluxe</h4><div class="burger-pic"><div class="photo" role="img" aria-label="Photo of a kiwi deluxe burger"></div><span class="price">K24.00</span></div></article>
      <article class="burger"><h4 class="item-name">Comet Patty</h4><div class="burger-pic"><div class="photo" role="img" aria-label="Photo of the house patty burger"></div><span class="price">K30.00</span></div></article>
      <article class="burger"><h4 class="item-name">The Hangover</h4><div class="burger-pic"><div class="photo" role="img" aria-label="Photo of a loaded hangover burger"></div><span class="price">K28.00</span></div></article>
      <article class="burger"><h4 class="item-name">Crunchy Chicken</h4><div class="burger-pic"><div class="photo" role="img" aria-label="Photo of a crunchy chicken burger"></div><span class="price">K30.00</span></div></article>
      <article class="burger"><h4 class="item-name">BLT + C Sandwich</h4><div class="burger-pic"><div class="photo" role="img" aria-label="Photo of a BLT sandwich"></div><span class="price">K14.00</span></div></article>
      <article class="burger"><h4 class="item-name">Steak Sandwich</h4><div class="burger-pic"><div class="photo" role="img" aria-label="Photo of a steak sandwich"></div><span class="price">K26.00</span></div></article>
    </div>

    <div class="upgrade-box">
      <div class="photo" role="img" aria-label="Photo of chips and a soft drink"></div>
      <div>
        <p class="upgrade-line">Upgrade to a meal deal – large <span class="price">K17.00</span></p>
        <p class="upgrade-line">Upgrade to a meal deal – small <span class="price">K12.00</span></p>
        <p class="upgrade-note">Chips and a soft drink, your choice of flavour</p>
      </div>
    </div>

    <h3 class="section-bar bar-maroon">Loaded Wedges</h3>
    <div class="mini-row two">
      <div class="mini">Loaded Wedges Plain<div class="mini-pic"><div class="photo" role="img" aria-label="Photo of plain loaded wedges"></div><span class="price">K15.00</span></div></div>
      <div class="mini">Loaded Wedges Chicken<div class="mini-pic"><div class="photo" role="img" aria-label="Photo of chicken loaded wedges"></div><span class="price">K18.00</span></div></div>
    </div>

    <h3 class="section-bar bar-cyan">Wraps</h3>
    <div class="mini-row">
      <div class="mini">Wraps – Veggie<div class="mini-pic"><div class="photo" role="img" aria-label="Photo of a veggie wrap"></div></div><span class="price">K18.00</span></div>
      <div class="mini">Wraps – Chicken<div class="mini-pic"><div class="photo" role="img" aria-label="Photo of a chicken wrap"></div></div><span class="price">K22.00</span></div>
      <div class="mini">Wraps – Lamb<div class="mini-pic"><div class="photo" role="img" aria-label="Photo of a lamb wrap"></div></div><span class="price">K30.00</span></div>
    </div>
  </section>

  <section class="column drinks">
    <h2 class="section-bar bar-orange">Dessert</h2>
    <div class="dessert">
      <div class="dessert-item"><div class="photo" role="img" aria-label="Photo of a soft serve sundae"></div><div><h4 class="item-name">Sundae</h4><span class="price">K4.00</span></div></div>
      <div class="dessert-item"><div class="photo cone" role="img" aria-label="Photo of a soft serve cone"></div><div><h4 class="item-name">Soft Cone</h4><span class="price">K2.00</span></div></div>
    </div>
    <div class="dessert-addons">
      <div>
        <h4>Add On's</h4>
        <p>Sprinkles K1.00 · Caramel K1.00<br>Chocolate K1.00 · Strawberry K1.00</p>
      </div>
      <div class="badge" aria-hidden="true"></div>
    </div>

    <h3 class="section-bar bar-red">Hot Beverages</h3>
    <ul class="drink-list">
      <li>Cappuccino <span class="price">K8.00</span></li>
      <li>Flat White <span class="price">K8.00</span></li>
      <li>Latte <span class="price">K8.00</span></li>
      <li>Hot Chocolate <span class="price">K8.00</span></li>
      <li>Mocha <span class="price">K8.00</span></li>
      <li>Long Black <span class="price">K6.50</span></li>
      <li>Babyccino <span class="price">K3.00</span></li>
      <li>Black Tea <span class="price">K4.50</span></li>
      <li>Extra Shot Coffee <span class="price">K2.00</span></li>
      <li>Extra Sugar <span class="price">K0.50</span></li>
    </ul>

    <h3 class="section-bar bar-green">Drinks</h3>
    <ul class="drink-list cold">
      <li>Soft Drink 600ml <span class="price">K6.00</span></li>
      <li>Soft Drink 1.5L <span class="price">K10.00</span></li>
      <li>Pure Water 750ml <span class="price">K3.50</span></li>
      <li>Pure Water 1.5L <span class="price">K5.00</span></li>
      <li>Fruit Juice 350ml <span class="price">K5.00</span></li>
      <li>Iced Tea <span class="price">K5.00</span></li>
      <li>Energy Drink <span class="price">K7.00</span></li>
      <li>Flavoured Milk <span class="price">K6.00</span></li>
    </ul>
  </section>

</main>
</body>
</html>
```